Ridgemont Business Card Redesign

Using the current logo/tagline lock-up and icon, redesign the Ridgemont business card to better show the tagline and improve the layout to give the card a more timely design and a classic, sophisticated look. See attached Project Brief for more detail.

```html
<!DOCTYPE html>
<html lang="en">
<head>
<meta charset="utf-8">
<title>Ridgemont Capital – Business Card</title>
<link rel="stylesheet" href="https://fonts.googleapis.com/css2?family=Jost:wght@400;500&family=Questrial&family=Libre+Baskerville:ital@1&display=swap">
<style>
  :root {
    --page: #fdfdfd;
    --card: #f1f1f1;
    --navy: #234a6e;
    --blue: #1b72c0;
    --ink: #4a4a4a;
    --muted: #8a8a8a;
  }
  html, body {
    margin: 0;
    width: 1200px;
    height: 1200px;
    overflow: hidden;
    background: var(--page);
  }
  .card {
    position: absolute;
    left: 180px;
    top: 360px;
    width: 840px;
    height: 480px;
    background: var(--card);
    overflow: hidden;
  }
  .accent {
    position: absolute;
    background: var(--navy);
  }
  .accent--corner {
    left: 0; top: -44px;
    width: 88px; height: 106px;
    border-radius: 0 0 44px 0;
  }
  .accent--top {
    left: 393px; top: -20px;
    width: 39px; height: 50px;
    border-radius: 0 0 20px 20px;
  }
  .accent--bottom {
    left: 393px; top: 450px;
    width: 39px; height: 50px;
    border-radius: 20px 20px 0 0;
  }
  .brand {
    position: absolute;
    left: 36px;
    top: 196px;
    display: flex;
    align-items: center;
    gap: 20px;
  }
  .brand__dot {
    width: 76px;
    height: 76px;
    border-radius: 50%;
    background: var(--blue);
    flex: none;
  }
  .brand__name {
    font-family: 'Jost', sans-serif;
    font-weight: 500;
    color: var(--ink);
    font-size: 30px;
    line-height: 1;
    letter-spacing: 4.5px;
    text-transform: uppercase;
    margin: 0;
  }
  .brand__sub {
    font-family: 'Jost', sans-serif;
    font-weight: 500;
    color: var(--ink);
    font-size: 16px;
    letter-spacing: 19px;
    text-transform: uppercase;
    margin: 6px 0 0;
    padding-bottom: 4px;
    border-bottom: 1px solid var(--ink);
  }
  .brand__tagline {
    font-family: 'Jost', sans-serif;
    color: var(--blue);
    font-size: 11px;
    letter-spacing: 1.9px;
    text-transform: uppercase;
    margin: 5px 0 0;
  }
  .contact {
    position: absolute;
    left: 476px;
    top: 109px;
    color: var(--ink);
  }
  .contact__name {
    font-family: 'Jost', sans-serif;
    font-weight: 500;
    font-size: 29px;
    margin: 0;
    line-height: 32px;
  }
  .contact__title {
    font-family: 'Libre Baskerville', serif;
    font-style: italic;
    font-size: 14.5px;
    color: var(--muted);
    text-align: center;
    width: 220px;
    margin: 0;
    line-height: 18px;
  }
  .contact__rule {
    width: 218px;
    margin-top: 6px;
  }
  .contact__rule span {
    display: block;
    height: 4px;
    border-radius: 2px;
  }
  .contact__rule .rule-navy { background: var(--navy); }
  .contact__rule .rule-blue { background: var(--blue); margin-top: 1px; }
  .contact__address {
    font-family: 'Questrial', sans-serif;
    font-style: normal;
    font-size: 19.5px;
    line-height: 24px;
    margin-top: 15px;
  }
  .contact__phone {
    display: flex;
    align-items: center;
    gap: 6px;
    font-family: 'Questrial', sans-serif;
    font-size: 17.5px;
    line-height: 22px;
    margin-top: 23px;
  }
  .contact__phone + .contact__phone { margin-top: 19px; }
  .contact__phone svg { flex: none; }
</style>
</head>
<body>
  <div class="card">
    <div class="accent accent--corner" role="img" aria-label="Decorative curved line motif"></div>
    <div class="accent accent--top" role="img" aria-label="Decorative curved line motif"></div>
    <div class="accent accent--bottom" role="img" aria-label="Decorative curved line motif"></div>

    <div class="brand">
      <div class="brand__dot"></div>
      <div>
        <p class="brand__name">Ridgemont</p>
        <p class="brand__sub">Capital</p>
        <p class="brand__tagline">Non-Control Growth Capital</p>
      </div>
    </div>

    <div class="contact">
      <h1 class="contact__name">Daniel R. Whitford</h1>
      <p class="contact__title">Principal &amp;<br>Chief Marketing Officer</p>
      <div class="contact__rule"><span class="rule-navy"></span><span class="rule-blue"></span></div>
      <address class="contact__address">41 Maple Crest Avenue<br>Suite 210<br>Milford, CT 06460</address>
      <div class="contact__phone">
        <svg width="22" height="20" viewBox="0 0 22 20" aria-hidden="true">
          <rect x="1" y="1" width="12" height="18" fill="none" stroke="#4a4a4a" stroke-width="1.5"/>
          <rect x="13" y="8" width="8" height="11" fill="none" stroke="#4a4a4a" stroke-width="1.5"/>
          <path d="M4 4h2M8 4h2M4 8h2M8 8h2M4 12h2M8 12h2M16 11h2M16 15h2" stroke="#4a4a4a" stroke-width="1.5"/>
        </svg>
        <span>(555) 310-2847</span>
      </div>
      <div class="contact__phone">
        <svg width="22" height="20" viewBox="0 0 22 20" aria-hidden="true">
          <rect x="1" y="1" width="11" height="18" rx="2" fill="none" stroke="#4a4a4a" stroke-width="1.5"/>
          <path d="M5 16h3" stroke="#4a4a4a" stroke-width="1.3"/>
          <path d="M15 7q2 3 0 6M18 5q3 5 0 10" fill="none" stroke="#4a4a4a" stroke-width="1.2"/>
        </svg>
        <span>(555) 614-9023</span>
      </div>
    </div>
  </div>
</body>
</html>
```